Business Card Design

We need new business card design. Website URL must be displayed in LARGE font as well as logo because we have B2B clients as well as B2C E-commerce store.
- B2B clients know us by our logo
- B2C clients know us by our website.
Please see the txt file for website details.
Find Logo file attached.
Do not use the logo from website.

```html
<!DOCTYPE html>
<html lang="en">
<head>
<meta charset="utf-8">
<title>Kappa Netlink – Business Card</title>
<link rel="stylesheet" href="https://fonts.googleapis.com/css2?family=Montserrat:wght@300;400;600;700&display=swap">
<style>
  :root {
    --canvas: #2f3236;
    --card-dark: #2a292a;
    --card-light: #ffffff;
    --accent: #2f9ad8;
    --ink-light: #ffffff;
    --ink-muted: #c9c9c9;
    --ink-dark: #2a292a;
  }
  * { box-sizing: border-box; margin: 0; padding: 0; }
  html, body {
    width: 1200px; height: 900px; overflow: hidden;
    background: var(--canvas);
    font-family: "Montserrat", Arial, sans-serif;
  }
  .stage {
    width: 1200px; height: 900px;
    display: flex; align-items: center; justify-content: center; gap: 60px;
  }
  .card {
    position: relative; width: 500px; height: 286px; overflow: hidden;
    box-shadow: 0 14px 30px rgba(0,0,0,.45);
  }

  /* Front */
  .card-front { background: var(--card-dark); }
  .stripes { position: absolute; width: 70px; }
  .stripes span { display: block; height: 5px; background: var(--accent); margin-bottom: 6px; }
  .stripes-top { top: 22px; left: 0; }
  .stripes-bottom { bottom: 17px; right: 0; }
  .front-content {
    position: absolute; inset: 0;
    display: flex; flex-direction: column; align-items: center; justify-content: center; gap: 26px;
  }
  .brand { display: flex; align-items: center; gap: 14px; }
  .brand-dot { width: 54px; height: 54px; border-radius: 50%; background: var(--accent); flex: none; }
  .brand-name {
    font-weight: 700; font-size: 40px; letter-spacing: 1px; color: var(--ink-light);
    text-transform: uppercase; line-height: 1; white-space: nowrap;
  }
  .website {
    display: flex; align-items: center; gap: 10px;
    color: var(--ink-light); font-size: 22px; font-weight: 400; letter-spacing: 4px;
  }
  .website svg { width: 22px; height: 22px; }

  /* Back */
  .card-back { background: var(--card-light); }
  .back-shape { position: absolute; inset: 0; width: 500px; height: 286px; }
  .contact { position: absolute; left: 28px; top: 26px; color: var(--ink-light); }
  .contact-name { font-size: 17px; font-weight: 300; letter-spacing: 1px; text-transform: uppercase; }
  .contact-name strong { font-weight: 700; }
  .contact-role { font-size: 11px; color: var(--ink-muted); letter-spacing: 2px; margin-top: 2px; }
  .contact-list { list-style: none; margin-top: 22px; }
  .contact-list li { display: flex; gap: 10px; align-items: flex-start; margin-bottom: 11px; }
  .contact-icon {
    width: 22px; height: 22px; background: var(--accent); flex: none;
    display: flex; align-items: center; justify-content: center;
  }
  .contact-icon svg { width: 13px; height: 13px; }
  .contact-text { font-size: 10.5px; line-height: 1.35; color: var(--ink-muted); }
  .back-brand { position: absolute; right: 28px; top: 140px; display: flex; align-items: center; gap: 10px; }
  .back-brand .brand-dot { width: 30px; height: 30px; }
  .back-brand .brand-name { font-size: 20px; color: var(--ink-dark); letter-spacing: .5px; }
</style>
</head>
<body>
<main class="stage">
  <section class="card card-front" aria-label="Card front">
    <div class="stripes stripes-top"><span></span><span></span></div>
    <div class="stripes stripes-bottom"><span></span><span></span></div>
    <div class="front-content">
      <div class="brand">
        <span class="brand-dot"></span>
        <span class="brand-name">Kappa Netlink</span>
      </div>
      <div class="website">
        <svg viewBox="0 0 24 24" fill="none" stroke="#fff" stroke-width="1.8">
          <circle cx="12" cy="12" r="10"/><ellipse cx="12" cy="12" rx="4.5" ry="10"/><line x1="2" y1="12" x2="22" y2="12"/>
        </svg>
        <span>WWW.KAPPALINK.GR</span>
      </div>
    </div>
  </section>

  <section class="card card-back" aria-label="Card back">
    <svg class="back-shape" viewBox="0 0 500 286" preserveAspectRatio="none">
      <path d="M0 0 H318 C290 100 196 125 176 286 H0 Z" fill="var(--accent)"/>
      <path d="M0 0 H300 C272 95 180 120 160 286 H0 Z" fill="var(--card-dark)"/>
    </svg>
    <div class="contact">
      <p class="contact-name">Daniel <strong>Marsh</strong></p>
      <p class="contact-role">DIRECTOR</p>
      <ul class="contact-list">
        <li>
          <span class="contact-icon"><svg viewBox="0 0 24 24" fill="#fff"><path d="M6.6 10.8a15 15 0 0 0 6.6 6.6l2.2-2.2a1 1 0 0 1 1-.25 11 11 0 0 0 3.6.6 1 1 0 0 1 1 1V20a1 1 0 0 1-1 1A17 17 0 0 1 3 4a1 1 0 0 1 1-1h3.5a1 1 0 0 1 1 1c0 1.25.2 2.45.6 3.6a1 1 0 0 1-.25 1z"/></svg></span>
          <span class="contact-text">+30 210-5550100<br>+30 210-5550190</span>
        </li>
        <li>
          <span class="contact-icon"><svg viewBox="0 0 24 24" fill="none" stroke="#fff" stroke-width="2"><circle cx="12" cy="12" r="9"/><ellipse cx="12" cy="12" rx="4" ry="9"/><line x1="3" y1="12" x2="21" y2="12"/></svg></span>
          <span class="contact-text">info@kappalink.gr<br>www.kappalink.gr</span>
        </li>
        <li>
          <span class="contact-icon"><svg viewBox="0 0 24 24" fill="#fff"><path d="M12 2a7 7 0 0 0-7 7c0 5 7 13 7 13s7-8 7-13a7 7 0 0 0-7-7zm0 9.5A2.5 2.5 0 1 1 12 6.5a2.5 2.5 0 0 1 0 5z"/></svg></span>
          <span class="contact-text">Harbor Ave. 120<br>10431 North Quarter</span>
        </li>
      </ul>
    </div>
    <div class="back-brand">
      <span class="brand-dot"></span>
      <span class="brand-name">KAPPA NETLINK</span>
    </div>
  </section>
</main>
</body>
</html>
```